Business Card Design Project

We are a commercial talent casting company, a very "now" company. We need a new business card that is both current, graphic and elegantly interesting. As we are a service business,
we need something that will attract the attention of new clients,
yet project a business that is 25 years old.

Industry/Entity Type

Business

Requirements
Must have
• 1. Logo - Nora Quillan Casting
2. Address - 47 Thornbury Street
New York, New York 10010
3. Phone - 212-738-4192
4. E-Mail - Casting@noraquillan.example

Nice to have
• Would like the card in black and white with the only accent
color being red.

```html
<!DOCTYPE html>
<html lang="en">
<head>
<meta charset="utf-8">
<title>Nora Quillan Casting — Business Card</title>
<link rel="stylesheet" href="https://fonts.googleapis.com/css2?family=Archivo:wght@400;500;800&display=swap">
<style>
  :root {
    --stage: #e9e9e9;
    --card-black: #1c1c1c;
    --card-black-edge: #0e0e0e;
    --card-white: #ffffff;
    --ink: #2a2a2a;
    --ink-soft: #4a4a4a;
    --logo-grey: #6b6e72;
    --accent-red: #d8261f;
    --band-black: #1a1a1a;
    --light-text: #f2f2f2;
  }
  * { box-sizing: border-box; margin: 0; padding: 0; }
  html, body { width: 1200px; height: 951px; overflow: hidden; }
  body {
    background: radial-gradient(ellipse at 50% 45%, #f7f7f7 0%, var(--stage) 70%, #d6d6d6 100%);
    font-family: "Archivo", Arial, sans-serif;
    position: relative;
  }
  .card {
    position: absolute;
    width: 640px;
    height: 366px;
    border-radius: 26px;
    overflow: hidden;
    box-shadow: 0 18px 40px rgba(0,0,0,0.22), 0 3px 8px rgba(0,0,0,0.15);
  }

  /* Front side */
  .card-front {
    left: 90px; top: 80px;
    background: radial-gradient(ellipse at 40% 30%, #343434 0%, var(--card-black) 55%, var(--card-black-edge) 100%);
  }
  .card-front .wordmark {
    position: absolute;
    left: 78px; top: 62px;
    font-weight: 800;
    font-size: 68px;
    line-height: 0.98;
    letter-spacing: 1px;
    color: var(--logo-grey);
    text-transform: uppercase;
  }
  .card-front .website {
    position: absolute;
    left: 82px; top: 300px;
    font-size: 17px;
    letter-spacing: 2.5px;
    color: var(--light-text);
  }

  /* Back side */
  .card-back {
    left: 470px; top: 500px;
    background: var(--card-white);
  }
  .card-back .wordmark {
    position: absolute;
    left: 48px; top: 38px;
    font-weight: 800;
    font-size: 42px;
    line-height: 0.98;
    letter-spacing: 0.5px;
    color: var(--logo-grey);
    text-transform: uppercase;
  }
  .person {
    position: absolute;
    right: 40px; top: 62px;
    text-align: right;
  }
  .person .name { font-size: 22px; font-weight: 500; color: var(--ink); }
  .person .role { font-size: 14px; color: var(--accent-red); margin-top: 4px; }

  .contact-row {
    display: flex; align-items: flex-start; gap: 10px;
    font-size: 17px; color: var(--ink-soft); line-height: 1.2;
  }
  .contact-row svg { flex: none; margin-top: 2px; }
  .address { position: absolute; left: 48px; top: 232px; }
  .lines { position: absolute; left: 356px; top: 232px; display: flex; flex-direction: column; gap: 4px; }

  .footer-band { position: absolute; left: 0; bottom: 0; width: 640px; height: 30px; }
</style>
</head>
<body>

  <section class="card card-front" aria-label="Card front">
    <h1 class="wordmark">Nora<br>Quillan<br>Casting</h1>
    <p class="website">www.noraquillan.example</p>
  </section>

  <section class="card card-back" aria-label="Card back">
    <div class="wordmark">Nora<br>Quillan<br>Casting</div>

    <div class="person">
      <div class="name">Peter Hallworth</div>
      <div class="role">director</div>
    </div>

    <div class="contact-row address">
      <svg width="16" height="16" viewBox="0 0 16 16" aria-hidden="true">
        <path d="M8 1 L15 8 H13 V15 H9.5 V10.5 H6.5 V15 H3 V8 H1 Z" fill="var(--accent-red)"/>
      </svg>
      <div>47 Thornbury Street<br>New York, New York 10010</div>
    </div>

    <div class="lines">
      <div class="contact-row">
        <svg width="16" height="16" viewBox="0 0 16 16" aria-hidden="true">
          <path d="M4 1.5 L6.5 4.5 L5 6.5 C6 8.5 7.5 10 9.5 11 L11.5 9.5 L14.5 12 L12.5 14.5 C7 14 2 9 1.5 3.5 Z" fill="var(--accent-red)"/>
        </svg>
        <span>212-738-4192</span>
      </div>
      <div class="contact-row">
        <svg width="16" height="16" viewBox="0 0 16 16" aria-hidden="true">
          <rect x="1" y="3" width="14" height="10" rx="1.5" fill="var(--accent-red)"/>
          <path d="M1.5 4 L8 9 L14.5 4" stroke="#fff" stroke-width="1.4" fill="none"/>
        </svg>
        <span>Casting@noraquillan.example</span>
      </div>
      <div class="contact-row">
        <svg width="16" height="16" viewBox="0 0 16 16" aria-hidden="true">
          <circle cx="8" cy="8" r="7" fill="var(--accent-red)"/>
        </svg>
        <span>www.noraquillan.example</span>
      </div>
    </div>

    <svg class="footer-band" viewBox="0 0 640 30" preserveAspectRatio="none" aria-hidden="true">
      <polygon points="0,10 420,10 400,30 0,30" fill="var(--band-black)"/>
      <polygon points="430,0 640,0 640,30 408,30" fill="var(--accent-red)"/>
    </svg>
  </section>

</body>
</html>
```